New funky, super creative logo design for printing business

Stamp, Wrap and Ship

We are a new digital printing business, based on the Gold Coast of Australia. We have a web site under construction - www.stampwrapandship.net, which will aim at the Business to Business market. We are digital printers, offering a wide variety of print products from business cards to wide format print jobs for consumers and small to medium sized business'. We offer up to date technological, digital and wide format print, at hi octane speed. Our prices are very competitive, and turnaround is super fast.

We like to think outside the box, and this should shine through in the design and colours that you use. Be bold and creative, we want to stand out from the crowd.

We will also soon be needing a full suite of marketing collaterals - posters, letterheads, scrap pads, calendars, banners etc. but this will come later, once we have decided on the logo and layouts.

We want a vibrant, bold image, communicating vibrancy and excitement.

Details on the card are company name: Stamp, Wrap and Ship.
www.stampwrapandship.net.
contact: Corinne (+61)437182265
e-mail:corinne@stampwrapandship.net

I must be able to change some of the details such as the name and number on the card.

Target Market(s)

Business to business, small retail, some individuals

Industry/Entity Type

Construction

Requirements
Must have
• Unique funky logo.
Nice to have
• A three dimensional look,with depth in the logo.

```html
<!DOCTYPE html>
<html lang="en">
<head>
<meta charset="utf-8">
<title>Stamp, Wrap and Ship – Business Card</title>
<link rel="stylesheet" href="https://fonts.googleapis.com/css2?family=Alfa+Slab+One&family=Arimo:wght@700&display=swap">
<style>
  :root {
    --backdrop: #5b5b5b;
    --card-light: #4a4a4a;
    --card-dark: #232323;
    --ink-white: #ffffff;
    --brand-magenta: #d7186f;
    --display-font: "Alfa Slab One", serif;
    --body-font: "Arimo", sans-serif;
  }
  * { margin: 0; padding: 0; box-sizing: border-box; }
  html, body { width: 1200px; height: 534px; overflow: hidden; }
  body { background: var(--backdrop); position: relative; }

  .card {
    position: absolute;
    top: 119px;
    width: 517px;
    height: 294px;
    overflow: hidden;
    background: radial-gradient(ellipse at 50% 45%, var(--card-light) 0%, var(--card-dark) 100%);
  }
  .card--front { left: 62px; }
  .card--back { left: 622px; }

  /* Front */
  .brand-lockup {
    position: absolute;
    left: 0; right: 0; top: 56px;
    display: flex; flex-direction: column; align-items: center;
  }
  .brand-dot {
    width: 122px; height: 122px;
    border-radius: 50%;
    background: var(--brand-magenta);
    margin-bottom: 20px;
  }
  .brand-name {
    font-family: var(--display-font);
    color: var(--ink-white);
    text-align: center;
    text-transform: uppercase;
    font-size: 24px;
    line-height: 24px;
    letter-spacing: 0.5px;
  }

  /* Back */
  .brand-disc {
    position: absolute;
    left: -110px; top: 0;
    width: 300px; height: 300px;
    border-radius: 50%;
    background: var(--brand-magenta);
  }
  .card-heading {
    position: absolute;
    right: 24px; top: 40px;
    font-family: var(--display-font);
    font-weight: 400;
    color: var(--ink-white);
    font-size: 21px;
    text-transform: uppercase;
    letter-spacing: 0.5px;
  }
  .contact {
    position: absolute;
    right: 24px; top: 180px;
    text-align right;
    text-align: right;
    font-family: var(--body-font);
    font-weight: 700;
    color: var(--ink-white);
    font-size: 13.5px;
    line-height: 25px;
  }
</style>
</head>
<body>
  <section class="card card--front" aria-label="Card front">
    <div class="brand-lockup">
      <span class="brand-dot" aria-hidden="true"></span>
      <p class="brand-name">Stamp, Wrap<br>and Ship</p>
    </div>
  </section>

  <section class="card card--back" aria-label="Card back">
    <span class="brand-disc" aria-hidden="true"></span>
    <h1 class="card-heading">Stamp, Wrap and Ship</h1>
    <div class="contact">
      <p class="contact-label">CONTACT</p>
      <p class="contact-name">Corinne (+61) 437182265</p>
      <p class="contact-email">e-mail: corinne@stampwrapandship.net</p>
    </div>
  </section>
</body>
</html>
```